Lanterne architecture business cards

We are a new company based in New Zealand. We Specialize in High end Luxury Residential Architecture.

Every home is bespoke and is designed to each clients individual requirements and needs.

I like to design buildings that inspire people through light and form while offering a high level of comfort and usability.

Lines of sight, proportion and balance are fundamental to the spaces I create.
Updates

August 5th is current deadline - Today's date is the 13th of August.

Target Market(s)

New Zealanders who want a custom individual home design, typically 30-65 year old males and females

Industry/Entity Type

Architecture

Contact Information for Business Card

Director - Derek Tolson
Contact Number - 0279164073
Email - info@lanternearchitecture-example.co.nz
Webstie - www.lanternearchitecture-example.co.nz
Social Media - @lanternearchitecture

Font styles to use
Sans Serif

Requirements
Must have
• Logo (Both Sides)
Website
Email
Contact Number
Social Media

Nice to have
• Texture
Should not have
• More than 3 colours - typically I would've thought 2 would be good to match the logo.

```html
<!DOCTYPE html>
<html lang="en">
<head>
<meta charset="utf-8">
<title>Lanterne Architecture – Business Cards</title>
<link href="https://fonts.googleapis.com/css2?family=Jost:wght@300;400;700&display=swap" rel="stylesheet">
<style>
  :root {
    --backdrop: #a9bcbc;
    --card: #070909;
    --ink: #ffffff;
    --ink-soft: #d9dcdc;
  }
  * { margin: 0; padding: 0; box-sizing: border-box; }
  html, body { width: 1200px; height: 960px; overflow: hidden; }
  body {
    background: var(--backdrop);
    font-family: "Jost", sans-serif;
    color: var(--ink);
    position: relative;
  }
  .card {
    position: absolute;
    left: 257px;
    width: 666px;
    height: 381px;
    background: var(--card);
  }
  .card--front { top: 49px; }
  .card--back { top: 507px; }
  .card__frame {
    position: absolute;
    inset: 18px 18px 17px 18px;
    border: 2.5px solid var(--ink);
  }
  .wordmark {
    position: absolute;
    text-align: center;
    font-weight: 300;
    text-transform: uppercase;
    white-space: nowrap;
    line-height: 1;
  }
  .wordmark__name, .wordmark__sub { display: block; }
  .card--front .wordmark { left: 153px; width: 360px; top: 165px; }
  .card--front .wordmark__name { font-size: 32px; letter-spacing: 24px; margin-right: -24px; }
  .card--front .wordmark__sub { font-size: 10px; letter-spacing: 24.5px; margin-right: -24.5px; margin-top: 14px; }
  .card--back .wordmark { left: 65px; width: 200px; top: 198px; }
  .card--back .wordmark__name { font-size: 19px; letter-spacing: 12.5px; margin-right: -12.5px; }
  .card--back .wordmark__sub { font-size: 6px; letter-spacing: 12.6px; margin-right: -12.6px; margin-top: 7px; color: var(--ink-soft); }
  .ruler { position: absolute; left: 18px; top: 18px; }
  .person { position: absolute; left: 356px; top: 50px; }
  .person__name { font-size: 24px; font-weight: 700; letter-spacing: 0.5px; line-height: 1; text-transform: uppercase; }
  .person__role { font-size: 17px; font-weight: 700; margin-top: 12px; line-height: 1; }
  .contact { position: absolute; left: 356px; top: 176px; list-style: none; }
  .contact__item { display: flex; align-items: center; height: 25px; font-size: 14px; font-weight: 300; }
  .contact__icon { width: 16px; height: 16px; margin-right: 12px; flex: none; }
  .social { position: absolute; left: 366px; width: 160px; top: 302px; text-align: center; }
  .social__handle { font-size: 14px; font-weight: 300; line-height: 1; }
  .social__dots { display: flex; justify-content: center; gap: 14px; margin-top: 11px; }
  .social__dot { width: 15px; height: 15px; border-radius: 50%; background: var(--ink-soft); }
</style>
</head>
<body>
  <section class="card card--front" aria-label="Business card front">
    <div class="card__frame"></div>
    <div class="wordmark">
      <span class="wordmark__name">Lanterne</span>
      <span class="wordmark__sub">Architecture</span>
    </div>
  </section>

  <section class="card card--back" aria-label="Business card back">
    <div class="card__frame"></div>
    <svg class="ruler" width="14" height="346" viewBox="0 0 14 346" aria-hidden="true">
      <g stroke="#ffffff" stroke-width="2">
        <line x1="1" y1="14" x2="9" y2="14"/><line x1="1" y1="22" x2="5" y2="22"/>
        <line x1="1" y1="30" x2="5" y2="30"/><line x1="1" y1="38" x2="9" y2="38"/>
        <line x1="1" y1="46" x2="5" y2="46"/><line x1="1" y1="54" x2="5" y2="54"/>
        <line x1="1" y1="62" x2="9" y2="62"/><line x1="1" y1="70" x2="5" y2="70"/>
        <line x1="1" y1="78" x2="5" y2="78"/><line x1="1" y1="86" x2="9" y2="86"/>
        <line x1="1" y1="94" x2="5" y2="94"/><line x1="1" y1="102" x2="5" y2="102"/>
        <line x1="1" y1="110" x2="9" y2="110"/><line x1="1" y1="118" x2="5" y2="118"/>
        <line x1="1" y1="126" x2="5" y2="126"/><line x1="1" y1="134" x2="9" y2="134"/>
        <line x1="1" y1="142" x2="5" y2="142"/><line x1="1" y1="150" x2="5" y2="150"/>
        <line x1="1" y1="158" x2="9" y2="158"/><line x1="1" y1="166" x2="5" y2="166"/>
        <line x1="1" y1="174" x2="5" y2="174"/><line x1="1" y1="182" x2="9" y2="182"/>
        <line x1="1" y1="190" x2="5" y2="190"/><line x1="1" y1="198" x2="5" y2="198"/>
        <line x1="1" y1="206" x2="9" y2="206"/><line x1="1" y1="214" x2="5" y2="214"/>
        <line x1="1" y1="222" x2="5" y2="222"/><line x1="1" y1="230" x2="9" y2="230"/>
        <line x1="1" y1="238" x2="5" y2="238"/><line x1="1" y1="246" x2="5" y2="246"/>
        <line x1="1" y1="254" x2="9" y2="254"/><line x1="1" y1="262" x2="5" y2="262"/>
        <line x1="1" y1="270" x2="5" y2="270"/><line x1="1" y1="278" x2="9" y2="278"/>
        <line x1="1" y1="286" x2="5" y2="286"/><line x1="1" y1="294" x2="5" y2="294"/>
        <line x1="1" y1="302" x2="9" y2="302"/><line x1="1" y1="310" x2="5" y2="310"/>
        <line x1="1" y1="318" x2="5" y2="318"/><line x1="1" y1="326" x2="9" y2="326"/>
      </g>
    </svg>

    <div class="wordmark">
      <span class="wordmark__name">Lanterne</span>
      <span class="wordmark__sub">Architecture</span>
    </div>

    <div class="person">
      <p class="person__name">Derek Tolson</p>
      <p class="person__role">Director</p>
    </div>

    <ul class="contact">
      <li class="contact__item">
        <svg class="contact__icon" viewBox="0 0 16 16" aria-hidden="true"><rect x="4" y="1" width="8" height="14" rx="1.2" fill="none" stroke="#fff" stroke-width="1.4"/><line x1="7" y1="12.5" x2="9" y2="12.5" stroke="#fff" stroke-width="1.2"/></svg>
        + 0279164073
      </li>
      <li class="contact__item">
        <svg class="contact__icon" viewBox="0 0 16 16" aria-hidden="true"><circle cx="8" cy="8" r="2.8" fill="none" stroke="#fff" stroke-width="1.6"/><path d="M10.8 6v3.2c0 1.6 2.9 1.6 2.9-1.2A5.7 5.7 0 1 0 11 13" fill="none" stroke="#fff" stroke-width="1.6"/></svg>
        info@lanternearchitecture-example.co.nz
      </li>
      <li class="contact__item">
        <svg class="contact__icon" viewBox="0 0 16 16" aria-hidden="true"><g fill="none" stroke="#fff" stroke-width="1.1"><circle cx="8" cy="8" r="6.5"/><ellipse cx="8" cy="8" rx="3" ry="6.5"/><line x1="1.5" y1="8" x2="14.5" y2="8"/><line x1="2.5" y1="4.8" x2="13.5" y2="4.8"/><line x1="2.5" y1="11.2" x2="13.5" y2="11.2"/></g></svg>
        www.lanternearchitecture-example.co.nz
      </li>
    </ul>

    <div class="social">
      <p class="social__handle">@lanternearchitecture</p>
      <div class="social__dots" aria-hidden="true">
        <span class="social__dot"></span><span class="social__dot"></span><span class="social__dot"></span><span class="social__dot"></span>
      </div>
    </div>
  </section>
</body>
</html>
```